Italian restaurant needs new site

Need to make our website better.

Must have reservation module

Must be able to sell wine tasting tours and wine pairing tours and intégrate with lumo desk

Blog

Social media

Wandermeter ranking and last review.

Number of Pages Required

1 page

Font styles to use
Serif

Requirements
Must have
• Reservation module
• Marketplace to buy wine pairings and gift certificates
• Wandermeter review
• Chatterbay posts
• All info from old site

```html
<!DOCTYPE html>
<html lang="en">
<head>
<meta charset="utf-8">
<title>Vinara Bistro — Italian Cuisine &amp; Wine Bar</title>
<link href="https://fonts.googleapis.com/css2?family=Playfair+Display:wght@400;700&family=Mulish:ital,wght@0,400;0,600;0,700;1,400&display=swap" rel="stylesheet">
<style>
:root{
  --wine:#8c1d24;
  --wine-dark:#6e151b;
  --ink:#222;
  --body:#555;
  --muted:#777;
  --white:#fff;
  --footer:#232323;
  --footer-line:#3b3b3b;
  --wood:#3a2619;
  --field:#fff;
  --gold:#f2b01e;
}
*{box-sizing:border-box;margin:0;padding:0}
html,body{width:1200px;height:3025px;overflow:hidden}
body{font-family:"Mulish",Arial,sans-serif;color:var(--body);background:#fff;position:relative}
.serif{font-family:"Playfair Display",Georgia,serif}
a{color:inherit;text-decoration:none}

/* Hero */
.hero{position:absolute;top:0;left:0;width:1200px;height:612px;
  background:radial-gradient(ellipse at 50% 60%,#6b4a34 0%,#3a2a20 45%,#1d1510 100%)}
.hero-photo{position:absolute;inset:0;background:linear-gradient(100deg,rgba(120,140,70,.35) 0%,rgba(0,0,0,0) 30%,rgba(0,0,0,0) 70%,rgba(190,120,60,.35) 100%)}
.topbar-contact{position:absolute;left:86px;top:18px;color:var(--white);font-size:13px;line-height:24px}
.topbar-contact svg{width:11px;height:11px;fill:var(--white);vertical-align:-1px;margin-right:4px}
.nav{position:absolute;right:86px;top:28px;display:flex;gap:34px;color:var(--white);font-size:14px}
.brand-badge{position:absolute;left:465px;top:-86px;width:270px;height:270px;border-radius:50%;
  background:var(--white);border:6px solid #d9d9d9;display:flex;align-items:flex-end;justify-content:center;padding-bottom:70px}
.brand-badge .brand-name{font-family:"Playfair Display",Georgia,serif;font-size:34px;color:var(--wine)}
.hero-brand{position:absolute;left:0;width:1200px;top:340px;text-align:center;
  font-family:"Playfair Display",Georgia,serif;font-size:64px;color:var(--white);letter-spacing:2px}

/* Welcome */
.welcome{position:absolute;top:612px;left:0;width:1200px;height:445px;text-align:center}
.welcome h1{font-family:"Playfair Display",Georgia,serif;font-weight:400;font-size:31px;color:var(--ink);margin-top:76px}
.welcome p{width:760px;margin:22px auto 0;font-size:12.5px;line-height:20px;color:var(--body)}
.btn{display:inline-block;background:var(--wine);color:var(--white);font-size:15px;border-radius:26px;height:52px;line-height:52px;padding:0 36px}
.welcome .btn{margin-top:36px;width:144px;padding:0}

/* Tours & reservation */
.split{position:absolute;top:1057px;left:0;width:1200px;height:500px}
.split-left{position:absolute;left:0;top:0;width:597px;height:500px;
  background:linear-gradient(120deg,#6a7a52 0%,#4d3b2c 45%,#3a2b22 100%)}
.split-right{position:absolute;left:597px;top:0;width:603px;height:500px;
  background:linear-gradient(90deg,#3d3028 0%,#2e2622 60%,#4a3c33 100%)}
.shade{position:absolute;inset:0;background:rgba(20,15,12,.45)}
.tours{position:absolute;left:86px;top:150px;width:380px;color:var(--white)}
.tours h2{font-family:"Playfair Display",Georgia,serif;font-weight:400;font-size:29px}
.tours p{font-size:12.5px;line-height:20px;margin-top:18px}
.tours .btn{margin-top:22px;width:144px;text-align:center;padding:0}
.reserve{position:absolute;left:680px;top:40px;width:434px;color:var(--white)}
.reserve h2{font-family:"Playfair Display",Georgia,serif;font-weight:400;font-size:29px;line-height:44px}
.form{display:grid;grid-template-columns:209px 209px;gap:16px 16px;margin-top:24px}
.field{height:46px;background:var(--field);border-radius:4px;color:#666;font-size:13px;
  display:flex;align-items:center;justify-content:space-between;padding:0 18px}
.field svg{width:12px;height:12px;stroke:#666;fill:none;stroke-width:2}
.send{margin:22px 0 0 auto;display:block;width:146px;text-align:center;padding:0;border:0;font-family:inherit}

/* Blog */
.blog{position:absolute;top:1557px;left:0;width:1200px;height:580px}
.blog h2{position:absolute;left:88px;top:82px;font-family:"Playfair Display",Georgia,serif;font-weight:400;font-size:31px;color:var(--ink)}
.pager{position:absolute;left:702px;top:103px;display:flex;gap:8px}
.pager span{width:24px;height:24px;border:1px solid #aaa;display:flex;align-items:center;justify-content:center}
.pager svg{width:8px;height:8px;stroke:#666;fill:none;stroke-width:2}
.post{position:absolute;top:156px;width:328px}
.post-image{height:175px;border:4px solid #fff;box-shadow:0 0 0 1px #ddd}
.post h3{font-size:15px;font-weight:600;color:var(--ink);margin-top:16px}
.post .date{font-size:11.5px;color:var(--ink);margin-top:10px}
.post p{font-size:11.5px;line-height:19px;color:var(--muted);margin-top:8px}
.post .more{font-size:11.5px;font-weight:700;color:var(--ink);margin-top:4px;display:block}
.social-feed{position:absolute;left:796px;top:156px;width:316px;height:305px;border:1px solid #ddd;background:#fff}
.feed-cover{height:178px;background:linear-gradient(135deg,#5a0d18,#a3263a 50%,#3c0a12);position:relative}
.feed-cover .thumb{position:absolute;left:12px;top:14px;width:60px;height:60px;background:#c9b49a;border:2px solid #fff}
.feed-cover .page-name{position:absolute;left:84px;top:14px;color:#fff;font-size:19px;font-weight:600}
.feed-cover .likes{position:absolute;left:84px;top:42px;color:#fff;font-size:14px}
.feed-cover .like-btn{position:absolute;left:12px;top:130px;background:#f4f4f4;border:1px solid #ccc;font-size:13px;font-weight:700;color:#333;padding:4px 8px;display:flex;align-items:center;gap:6px}
.like-btn i{width:12px;height:12px;background:#4a66a0;border-radius:2px;display:inline-block}
.feed-body{padding:14px 18px;font-size:13.5px;color:#4a66a0;line-height:19px}
.friends{display:flex;gap:6px;margin-top:10px}
.friends span{width:42px;height:42px;background:linear-gradient(#b9a79a,#7d6a5e)}

/* Reviews */
.reviews{position:absolute;top:2137px;left:0;width:1200px;height:418px;
  background:linear-gradient(90deg,#2c1d13,#4a3120 50%,#2c1d13)}
.reviews-badge{position:absolute;left:0;width:1200px;top:34px;text-align:center;color:var(--white);font-size:18px;font-weight:600}
.reviews-badge i{display:inline-block;width:14px;height:14px;border-radius:50%;background:#34a873;margin-right:6px;vertical-align:-1px}
.reviews h2{position:absolute;left:0;width:1200px;top:66px;text-align:center;font-family:"Playfair Display",Georgia,serif;font-weight:400;font-size:31px;color:var(--white)}
.review{position:absolute;top:168px;width:335px;height:170px;border:2px solid rgba(255,255,255,.6)}
.quote-mark{position:absolute;left:-6px;top:-20px;width:40px;height:40px;border-radius:50%;background:#fff;display:flex;align-items:center;justify-content:center}
.quote-mark svg{width:18px;height:16px;fill:#333}
.review p{position:absolute;left:14px;right:12px;top:30px;font-style:italic;font-size:12px;line-height:23px;color:var(--white)}
.review .avatar{position:absolute;left:36px;top:128px;width:64px;height:64px;border-radius:50%;background:linear-gradient(#9c8678,#5e4a3e);border:3px solid #fff}
.review .who{position:absolute;left:130px;top:120px;color:var(--white);font-size:14px;font-weight:700}
.review .stars{position:absolute;left:130px;top:140px;display:flex;gap:4px}
.stars svg{width:14px;height:14px;fill:var(--gold)}
.arrow{position:absolute;top:2385px;width:16px;height:20px}
.arrow svg{width:16px;height:20px;stroke:#fff;fill:none;stroke-width:2.5}

/* Footer */
.footer{position:absolute;top:2555px;left:0;width:1200px;height:470px;background:var(--footer);color:#ddd}
.col{position:absolute;top:78px}
.col h4{font-size:17px;font-weight:400;letter-spacing:.5px;color:#fff;padding-bottom:18px;border-bottom:1px solid var(--footer-line);width:244px}
.contact-row{display:flex;gap:22px;font-size:13px;line-height:20px;color:#ddd;margin-top:22px}
.contact-row svg{width:12px;height:12px;fill:#fff;flex:none;margin-top:4px}
.socials{display:flex;gap:12px;margin-top:26px;flex-wrap:wrap;width:260px}
.socials span{display:flex;align-items:center;gap:5px;font-size:11px;color:#ddd}
.socials i{width:12px;height:12px;border-radius:50%;background:var(--wine);display:inline-block}
.newsletter p{font-size:13px;line-height:22px;margin-top:28px;color:#ddd}
.newsletter .email{margin-top:18px;width:252px;height:42px;background:#fff;color:#888;font-size:11px;display:flex;align-items:center;padding:0 14px}
.newsletter .submit{margin-top:10px;width:252px;height:42px;background:var(--wine);color:#fff;font-size:16px;font-weight:700;display:flex;align-items:center;justify-content:center}
.hours{font-size:13px;margin-top:28px}
.quick{margin-top:48px}
.quick ul{list-style:none;font-size:13px;line-height:26px;margin-top:20px}
.footer-rule{position:absolute;left:86px;right:86px;top:395px;border-top:1px solid var(--footer-line)}
.copyright{position:absolute;left:0;width:1200px;top:420px;text-align:center;font-size:13px;color:#ccc}
</style>
</head>
<body>

<header class="hero">
  <div class="hero-photo" role="img" aria-label="Close-up photograph of plated Italian dishes with grilled meat and vegetables"></div>
  <div class="topbar-contact">
    <div><svg viewBox="0 0 24 24"><path d="M6.6 10.8a15 15 0 0 0 6.6 6.6l2.2-2.2a1 1 0 0 1 1-.25 11.4 11.4 0 0 0 3.6.57 1 1 0 0 1 1 1V20a1 1 0 0 1-1 1A17 17 0 0 1 3 4a1 1 0 0 1 1-1h3.5a1 1 0 0 1 1 1c0 1.25.2 2.45.57 3.57a1 1 0 0 1-.25 1z"/></svg>155 2047</div>
    <div><svg viewBox="0 0 24 24"><path d="M12 2a7 7 0 0 0-7 7c0 5.2 7 13 7 13s7-7.8 7-13a7 7 0 0 0-7-7zm0 9.5A2.5 2.5 0 1 1 12 6.5a2.5 2.5 0 0 1 0 5z"/></svg>Calle Olivo 12, Centro, Cabo San Lucas, Mexico</div>
  </div>
  <div class="brand-badge"><span class="brand-name">Vinara Bistro</span></div>
  <nav class="nav"><a>Home</a><a>Menu</a><a>Reservations</a><a>Contact Us</a></nav>
  <div class="hero-brand">Vinara Bistro</div>
</header>

<section class="welcome">
  <h1>Welcome to Vinara Bistro</h1>
  <p>Sed ut perspiciatis unde omnis iste natus error sit voluptatem accusantium doloremque laudantium, totam rem aperiam, eaque ipsa quae ab illo inventore veritatis et quasi architecto beatae vitae dicta sunt explicabo. Nemo enim ipsam voluptatem quia voluptas sit aspernatur aut odit aut fugit, sed quia consequuntur magni dolores eos qui ratione voluptatem sequi nesciunt. Neque porro quisquam est, qui dolorem ipsum quia dolor sit amet, consectetur, adipisci velit, sed quia non numquam eius modi tempora incidunt ut labore et dolore magnam aliquam quaerat voluptatem. Ut enim ad minima veniam, quis nostrum exercitationem ullam corporis suscipit laboriosam,</p>
  <a class="btn">Read More</a>
</section>

<section class="split">
  <div class="split-left" role="img" aria-label="Photograph of friends raising glasses at an outdoor wine tasting"><div class="shade"></div></div>
  <div class="split-right" role="img" aria-label="Photograph of guests toasting with red wine glasses"><div class="shade"></div></div>
  <div class="tours">
    <h2>Wine Tasting Tours</h2>
    <p>Sed ut perspiciatis unde omnis iste natus error sit voluptatem accusantium doloremque laudantium, totam rem aperiam, eaque ipsa quae ab illo inventore veritatis</p>
    <a class="btn">Read More</a>
  </div>
  <div class="reserve">
    <h2>Reservations for Vinara bistro<br>&nbsp;Cabo San Lucas</h2>
    <div class="form">
      <div class="field">Date <svg viewBox="0 0 12 12"><rect x="1" y="2" width="10" height="9"/><path d="M1 5h10M4 1v2M8 1v2"/></svg></div>
      <div class="field">Time <svg viewBox="0 0 12 12"><circle cx="6" cy="6" r="5"/><path d="M6 3v3h2"/></svg></div>
      <div class="field">Party Size</div>
      <div class="field">Name</div>
      <div class="field">Email</div>
      <div class="field">Phone Number</div>
      <div class="field">Hotel Name <svg viewBox="0 0 12 12"><path d="M3 4.5l3 3 3-3"/></svg></div>
      <div class="field">Room Number <svg viewBox="0 0 12 12"><path d="M3 4.5l3 3 3-3"/></svg></div>
    </div>
    <a class="btn send">SEND</a>
  </div>
</section>

<section class="blog">
  <h2>Recent Blog Posts</h2>
  <div class="pager">
    <span><svg viewBox="0 0 8 8"><path d="M5.5 1L2.5 4l3 3"/></svg></span>
    <span><svg viewBox="0 0 8 8"><path d="M2.5 1l3 3-3 3"/></svg></span>
  </div>
  <article class="post" style="left:88px">
    <div class="post-image" role="img" aria-label="Photograph of red wine being poured into a glass" style="background:linear-gradient(135deg,#7a2a14,#b4502a 50%,#5a1c0c)"></div>
    <h3>De Finibus Bonorum et Malorum", written</h3>
    <div class="date">24 July, 2017</div>
    <p>Who would have imagined record market highs at this point last year, when the indices ended the year in negative territory? Or when new year...</p>
    <a class="more">More</a>
  </article>
  <article class="post" style="left:437px">
    <div class="post-image" role="img" aria-label="Photograph of two hands clinking red wine glasses" style="background:linear-gradient(135deg,#e8ddd2,#c9b29e 50%,#8a2a2a)"></div>
    <h3>De Finibus Bonorum et Malorum BC</h3>
    <div class="date">24 July, 2017</div>
    <p>If we could make a broad statement about stock investors, it would be that they have to be generally optimistic about the future. If stock...</p>
    <a class="more">More</a>
  </article>
  <aside class="social-feed">
    <div class="feed-cover" role="img" aria-label="Chatterbay page cover image in deep red tones">
      <div class="thumb"></div>
      <div class="page-name">Vinara Bistro</div>
      <div class="likes">3.464 Me gusta</div>
      <div class="like-btn"><i></i>Chatterbay · Me gusta esta página</div>
    </div>
    <div class="feed-body">
      Sé el primero de tus amigos en indicar que te gusta esto.
      <div class="friends" role="img" aria-label="Small profile thumbnails of page followers"><span></span><span></span><span></span><span></span><span></span></div>
    </div>
  </aside>
</section>

<section class="reviews" role="region" aria-label="Guest reviews">
  <div class="reviews-badge"><i></i>Wandermeter</div>
  <h2>Our Clients Says</h2>
  <div class="review" style="left:85px">
    <div class="quote-mark"><svg viewBox="0 0 18 16"><path d="M0 16V9C0 4 2 1 7 0v3C4.5 4 4 6 4 8h3v8zM11 16V9c0-5 2-8 7-9v3c-2.5 1-3 3-3 5h3v8z"/></svg></div>
    <p>We went to Vinara Bistro the third night of our stay. The entire staff was very attentive, the food was amazing and we will definitely be back. If you're looking to ...</p>
    <div class="avatar" role="img" aria-label="Reviewer profile photo"></div>
    <div class="who">Travelmum77</div>
    <div class="stars"><svg viewBox="0 0 24 24"><path d="M12 2l3 7 7 .6-5.3 4.7 1.7 7.2L12 17.8 5.6 21.5l1.7-7.2L2 9.6 9 9z"/></svg><svg viewBox="0 0 24 24"><path d="M12 2l3 7 7 .6-5.3 4.7 1.7 7.2L12 17.8 5.6 21.5l1.7-7.2L2 9.6 9 9z"/></svg><svg viewBox="0 0 24 24"><path d="M12 2l3 7 7 .6-5.3 4.7 1.7 7.2L12 17.8 5.6 21.5l1.7-7.2L2 9.6 9 9z"/></svg><svg viewBox="0 0 24 24"><path d="M12 2l3 7 7 .6-5.3 4.7 1.7 7.2L12 17.8 5.6 21.5l1.7-7.2L2 9.6 9 9z"/></svg><svg viewBox="0 0 24 24"><path d="M12 2l3 7 7 .6-5.3 4.7 1.7 7.2L12 17.8 5.6 21.5l1.7-7.2L2 9.6 9 9z"/></svg></div>
  </div>
  <div class="review" style="left:430px">
    <div class="quote-mark"><svg viewBox="0 0 18 16"><path d="M0 16V9C0 4 2 1 7 0v3C4.5 4 4 6 4 8h3v8zM11 16V9c0-5 2-8 7-9v3c-2.5 1-3 3-3 5h3v8z"/></svg></div>
    <p>I have extensive experience working within fine dining Italian cuisine establishments and this place holds up even to the places I've traveled in Italy...</p>
    <div class="avatar" role="img" aria-label="Reviewer profile photo"></div>
    <div class="who">Clara M.</div>
    <div class="stars"><svg viewBox="0 0 24 24"><path d="M12 2l3 7 7 .6-5.3 4.7 1.7 7.2L12 17.8 5.6 21.5l1.7-7.2L2 9.6 9 9z"/></svg><svg viewBox="0 0 24 24"><path d="M12 2l3 7 7 .6-5.3 4.7 1.7 7.2L12 17.8 5.6 21.5l1.7-7.2L2 9.6 9 9z"/></svg><svg viewBox="0 0 24 24"><path d="M12 2l3 7 7 .6-5.3 4.7 1.7 7.2L12 17.8 5.6 21.5l1.7-7.2L2 9.6 9 9z"/></svg><svg viewBox="0 0 24 24"><path d="M12 2l3 7 7 .6-5.3 4.7 1.7 7.2L12 17.8 5.6 21.5l1.7-7.2L2 9.6 9 9z"/></svg><svg viewBox="0 0 24 24"><path d="M12 2l3 7 7 .6-5.3 4.7 1.7 7.2L12 17.8 5.6 21.5l1.7-7.2L2 9.6 9 9z"/></svg></div>
  </div>
  <div class="review" style="left:775px">
    <div class="quote-mark"><svg viewBox="0 0 18 16"><path d="M0 16V9C0 4 2 1 7 0v3C4.5 4 4 6 4 8h3v8zM11 16V9c0-5 2-8 7-9v3c-2.5 1-3 3-3 5h3v8z"/></svg></div>
    <p>Who would have thought to even consider Italian food while in Mexico? Definitely not us. But we went with the reviews and they were exact. We safely...</p>
    <div class="avatar" role="img" aria-label="Reviewer profile photo"></div>
    <div class="who">dunes_2012</div>
    <div class="stars"><svg viewBox="0 0 24 24"><path d="M12 2l3 7 7 .6-5.3 4.7 1.7 7.2L12 17.8 5.6 21.5l1.7-7.2L2 9.6 9 9z"/></svg><svg viewBox="0 0 24 24"><path d="M12 2l3 7 7 .6-5.3 4.7 1.7 7.2L12 17.8 5.6 21.5l1.7-7.2L2 9.6 9 9z"/></svg><svg viewBox="0 0 24 24"><path d="M12 2l3 7 7 .6-5.3 4.7 1.7 7.2L12 17.8 5.6 21.5l1.7-7.2L2 9.6 9 9z"/></svg><svg viewBox="0 0 24 24"><path d="M12 2l3 7 7 .6-5.3 4.7 1.7 7.2L12 17.8 5.6 21.5l1.7-7.2L2 9.6 9 9z"/></svg><svg viewBox="0 0 24 24"><path d="M12 2l3 7 7 .6-5.3 4.7 1.7 7.2L12 17.8 5.6 21.5l1.7-7.2L2 9.6 9 9z"/></svg></div>
  </div>
</section>
<span class="arrow" style="left:28px"><svg viewBox="0 0 16 20"><path d="M11 3L4 10l7 7"/></svg></span>
<span class="arrow" style="left:1148px"><svg viewBox="0 0 16 20"><path d="M5 3l7 7-7 7"/></svg></span>

<footer class="footer">
  <div class="col" style="left:86px">
    <h4>GET IN TOUCH</h4>
    <div class="contact-row" style="margin-top:34px"><svg viewBox="0 0 24 24"><path d="M12 2a7 7 0 0 0-7 7c0 5.2 7 13 7 13s7-7.8 7-13a7 7 0 0 0-7-7zm0 9.5A2.5 2.5 0 1 1 12 6.5a2.5 2.5 0 0 1 0 5z"/></svg><span>Calle Olivo 12, Centro<br>Cabo San Lucas, Mexico</span></div>
    <div class="contact-row"><svg viewBox="0 0 24 24"><path d="M6.6 10.8a15 15 0 0 0 6.6 6.6l2.2-2.2a1 1 0 0 1 1-.25 11.4 11.4 0 0 0 3.6.57 1 1 0 0 1 1 1V20a1 1 0 0 1-1 1A17 17 0 0 1 3 4a1 1 0 0 1 1-1h3.5a1 1 0 0 1 1 1c0 1.25.2 2.45.57 3.57a1 1 0 0 1-.25 1z"/></svg><span>155 2047</span></div>
    <div class="contact-row"><svg viewBox="0 0 24 24"><path d="M2 5h20v14H2zm2 2v.5l8 5 8-5V7z"/></svg><span>info@vinarabistro.com</span></div>
    <div class="socials"><span><i></i>Chatterbay</span><span><i></i>Chirpline</span><span><i></i>Circlo</span><span><i></i>Reelbox</span><span><i></i>Snapgrid</span></div>
  </div>
  <div class="col newsletter" style="left:472px">
    <h4>NEWSLETTER SIGN UP</h4>
    <p>Don't miss our news and updates.<br>Subscribe now!</p>
    <div class="email">Enter Email</div>
    <div class="submit">SUBMIT</div>
  </div>
  <div class="col" style="left:865px">
    <h4>OUR OFFICE HOURS</h4>
    <div class="hours">Open daily from 5 to 12 am</div>
    <div class="quick">
      <h4>QUICK LINK</h4>
      <ul><li>&gt; Home</li><li>&gt; Menu</li><li>&gt; Reservations</li></ul>
    </div>
  </div>
  <div class="footer-rule"></div>
  <div class="copyright">Copyright © 2017. Vinara Bistro, Inc. All rights reserved</div>
</footer>

</body>
</html>
```